Modern Quillby Tree Care Website

I need a website for a full service Tree Care company. The company provides tree pruning, tree removal, tree preservation, emergency services, stump grinding, and emergency tree services.

Target Market(s)

Customers that need tree services

Industry/Entity Type

Landscaping, Tree Services

Coding

Coded - Design and coding required

Number of Pages Required

5+ page

Font styles to use
Sans Serif

Requirements
Must have
• Good clean design that showcases the services the company provides.
Nice to have
• Services page; contact form, blog, home page, about page

```html
<!DOCTYPE html>
<html lang="en">
<head>
<meta charset="utf-8">
<title>Quillby Tree Care</title>
<link href="https://fonts.googleapis.com/css2?family=Figtree:wght@400;500;600;700&display=swap" rel="stylesheet">
<style>
:root{
  --stage:#ececec;
  --cream:#fbf8ef;
  --white:#ffffff;
  --green:#79b540;
  --green-light:#eef8e3;
  --forest:#2f4a23;
  --orange:#f6a532;
  --footer:#35351f;
  --ink:#2a2a26;
  --muted:#5c5c55;
  --line:#dcdcd2;
}
*{box-sizing:border-box;margin:0;padding:0}
html,body{width:1200px;height:3358px;overflow:hidden}
body{background:var(--stage);font-family:"Figtree",sans-serif;color:var(--ink)}
.page{position:absolute;left:25px;top:190px;width:1150px;background:var(--white);border-radius:14px;overflow:hidden;box-shadow:0 6px 30px rgba(0,0,0,.06)}
.wordmark{font-weight:700;color:var(--forest);display:flex;align-items:center;gap:10px;white-space:nowrap}
.wordmark .dot{width:22px;height:22px;background:var(--green);border-radius:4px}

/* nav */
.nav{height:83px;background:var(--cream);display:flex;align-items:center;padding:0 100px;white-space:nowrap}
.nav .wordmark{font-size:24px;width:310px;flex:none}
.nav ul{display:flex;list-style:none;gap:30px;font-size:11px;font-weight:600;letter-spacing:.02em;flex:none}
.nav li.active{color:var(--orange);border-bottom:2px solid var(--green);padding-bottom:6px;margin-top:8px}
.nav .phone{color:var(--orange);font-size:13px;font-weight:600;margin-left:40px;display:flex;gap:6px;align-items:center;flex:none}
.btn{display:inline-block;font-weight:600;font-size:11px;color:#fff;padding:10px 16px;white-space:nowrap}
.btn-green{background:var(--green)}
.btn-orange{background:var(--orange)}
.btn-forest{background:var(--forest)}
.nav .btn{margin-left:28px;flex:none}

/* hero */
.hero{height:478px;position:relative;background:linear-gradient(110deg,#2c241b 0%,#4a3a2b 45%,#6b5540 70%,#3a2f24 100%)}
.hero-copy{position:absolute;left:190px;top:150px;color:#fff}
.hero h1{font-size:40px;font-weight:600;line-height:1.12}
.hero p{font-size:18px;margin:24px 0 26px}
.hero .btn{padding:12px 16px}
.dots{position:absolute;left:946px;top:196px;display:flex;flex-direction:column;gap:13px}
.dots span{width:11px;height:11px;border-radius:50%;background:#fff}
.dots span.on{background:var(--orange)}

/* services */
.services{height:670px;background:var(--cream);text-align:center;padding-top:70px}
.section-title{font-size:36px;font-weight:500}
.grid{display:grid;grid-template-columns:repeat(3,240px);gap:20px 24px;justify-content:center;margin-top:26px}
.card{text-align:left}
.card .ph{height:150px}
.card .label{height:38px;display:flex;justify-content:space-between;align-items:center;padding:0 12px;font-size:13px;font-weight:500;border-bottom:2px solid var(--line)}
.card.active .label{background:var(--green);color:#fff;border-color:var(--green)}
.services .btn{margin-top:32px;padding:10px 20px}

/* why */
.why{height:530px;text-align:center;padding-top:62px}
.features{display:flex;flex-wrap:wrap;justify-content:center;gap:22px;width:780px;margin:38px auto 0}
.feature{width:176px;height:136px;background:#fff;box-shadow:0 3px 16px rgba(0,0,0,.07);border-radius:6px;display:flex;flex-direction:column;align-items:center;padding-top:20px;font-size:11px;font-weight:500;line-height:1.2}
.feature svg{margin-bottom:12px}

/* call band */
.callband{height:341px;background:var(--forest);position:relative;color:#fff}
.callband .ph{position:absolute;right:0;top:0;width:560px;height:100%;clip-path:polygon(28% 0,100% 0,100% 100%,0 100%)}
.callband .copy{position:absolute;left:101px;top:82px}
.callband h2{font-size:24px;font-weight:400;line-height:1.2}
.callband h2 b{font-weight:700}
.callband .numbers{font-size:30px;color:var(--green);margin:22px 0 30px;display:flex;align-items:center;gap:14px;white-space:nowrap}
.callband .btn{padding:12px 16px;font-size:10px}

/* about */
.about{height:533px;position:relative}
.about .copy{position:absolute;left:190px;top:126px;width:370px}
.about h2{font-size:36px;font-weight:500}
.about .lead{font-size:13px;font-weight:700;margin:22px 0 24px;line-height:1.35}
.about .body{font-size:9.5px;line-height:1.9;color:var(--muted)}
.about .btn{margin-top:34px;padding:12px 28px;font-size:11px}
.estimate{position:absolute;left:587px;top:70px;width:371px;height:387px;background:linear-gradient(180deg,#fbfcf7,var(--green-light));box-shadow:0 4px 20px rgba(0,0,0,.07);padding:46px 24px 0;text-align:center}
.estimate h3{font-size:29px;font-weight:500;margin-bottom:28px}
.fields{display:grid;grid-template-columns:1fr 1fr;gap:13px 14px}
.field{background:#fff;height:34px;font-size:10px;color:var(--muted);text-align:left;padding:11px 16px}
.field.wide{grid-column:1/3}
.estimate .terms{font-size:10px;margin:18px 0 16px}
.estimate .terms u{font-weight:700}
.estimate .btn{padding:11px 36px}

/* footer */
.footer{height:342px;background:var(--footer);color:#fff;position:relative}
.footer .wordmark{position:absolute;left:190px;top:86px;color:var(--green);font-size:24px}
.fcol{position:absolute;top:78px;font-size:11px;line-height:2;white-space:nowrap}
.fcol h4{color:var(--green);font-size:12px;font-weight:600;margin-bottom:6px}
.fcol .row{display:flex;gap:8px;align-items:center}
.fcol.small{font-size:9.5px;line-height:2.25}
.socials{position:absolute;left:942px;top:76px;display:flex;flex-direction:column;gap:13px}
.socials span{width:26px;height:26px;border-radius:50%;background:#fff;display:block}
.socials span.on{background:var(--green)}
.footer .rule{position:absolute;left:190px;right:190px;top:262px;border-top:1px solid #55553f}
.footer .copy{position:absolute;left:0;right:0;top:296px;text-align:center;font-size:10px}
.footer .copy b{color:var(--green);font-weight:500}
</style>
</head>
<body>
<main class="page">

  <header class="nav">
    <div class="wordmark"><span class="dot"></span>Quillby Tree Care</div>
    <ul>
      <li class="active">HOME</li><li>ABOUT US</li><li>SERVICES</li><li>BLOG</li><li>CONTACT US</li>
    </ul>
    <span class="phone"><svg width="12" height="12" viewBox="0 0 24 24"><path d="M6 2l4 4-2 3c1 3 4 6 7 7l3-2 4 4-3 4C10 21 3 14 2 5z" fill="none" stroke="currentColor" stroke-width="2"/></svg>(555) 014-2739</span>
    <span class="btn btn-green">Get a Free Estimate</span>
  </header>

  <section class="hero" role="img" aria-label="Arborist cutting a log with a chainsaw in a wooded yard">
    <div class="hero-copy">
      <h1>Call QUILLBY for All Your<br>Tree Care Needs</h1>
      <p>Serving Fernvale and surrounding areas</p>
      <span class="btn btn-orange">Get a Free Estimate</span>
    </div>
    <div class="dots"><span></span><span class="on"></span><span></span><span></span></div>
  </section>

  <section class="services">
    <h2 class="section-title">We Provides Full Services for Tree Care</h2>
    <div class="grid">
      <div class="card active"><div class="ph" role="img" aria-label="Gloved hands pruning a tree branch" style="background:linear-gradient(135deg,#8a7f78,#c9c3bd)"></div><div class="label">Tree Pruning<span>↗</span></div></div>
      <div class="card"><div class="ph" role="img" aria-label="Chainsaw cutting a fallen tree" style="background:linear-gradient(135deg,#3b4a2c,#7b6a4f)"></div><div class="label">Tree Removal<span>↗</span></div></div>
      <div class="card"><div class="ph" role="img" aria-label="Hands planting a young tree in soil" style="background:linear-gradient(135deg,#4a5a34,#6a4f3a)"></div><div class="label">Tree Preservation<span>↗</span></div></div>
      <div class="card"><div class="ph" role="img" aria-label="Arborist in safety gear working up a tree" style="background:linear-gradient(135deg,#c9c6c0,#5c4a36)"></div><div class="label">Emergency Tree Services<span>↗</span></div></div>
      <div class="card"><div class="ph" role="img" aria-label="Cut logs and sawdust on the ground" style="background:linear-gradient(135deg,#5a4534,#c6a58a)"></div><div class="label">Stump Grinding<span>↗</span></div></div>
      <div class="card"><div class="ph" role="img" aria-label="Fallen branches across a road after a storm" style="background:linear-gradient(135deg,#556b3a,#8a8a7a)"></div><div class="label">Strom Damage Cleanup<span>↗</span></div></div>
    </div>
    <span class="btn btn-forest">View All Services</span>
  </section>

  <section class="why">
    <h2 class="section-title">Why Choose Quillby Tree Care</h2>
    <div class="features">
      <div class="feature"><svg width="44" height="48" viewBox="0 0 44 48" fill="none" stroke="#2f4a23" stroke-width="2"><rect x="6" y="4" width="26" height="36" rx="2"/><path d="M12 14h14M12 20h14M12 26h8"/><path d="M30 28l8 3v6c0 4-4 7-8 8-4-1-8-4-8-8v-6z" fill="#79b540"/></svg>Licensed and<br>insured</div>
      <div class="feature"><svg width="44" height="48" viewBox="0 0 44 48" fill="none" stroke="#2f4a23" stroke-width="2"><rect x="10" y="6" width="20" height="36" rx="3"/><path d="M17 36h6"/><circle cx="32" cy="12" r="8" fill="#79b540" stroke="none"/></svg>24-Hours emergency<br>services</div>
      <div class="feature"><svg width="44" height="48" viewBox="0 0 44 48" fill="none" stroke="#2f4a23" stroke-width="2"><path d="M22 42s-12-13-12-22a12 12 0 0124 0c0 9-12 22-12 22z"/><circle cx="22" cy="20" r="5" fill="#79b540"/><path d="M8 44h28"/></svg>Locally owned and<br>operated</div>
      <div class="feature"><svg width="44" height="48" viewBox="0 0 44 48" fill="none" stroke="#2f4a23" stroke-width="2"><circle cx="22" cy="16" r="10" fill="#79b540"/><path d="M22 16v16M8 34h28v8H8z"/></svg>Professional<br>work</div>
      <div class="feature"><svg width="44" height="48" viewBox="0 0 44 48" fill="none" stroke="#2f4a23" stroke-width="2"><path d="M22 4l16 6v12c0 10-8 18-16 22C14 40 6 32 6 22V10z"/><circle cx="22" cy="22" r="9" fill="#79b540"/><path d="M18 22l3 3 5-6" stroke="#fff"/></svg>Safety is our no.1<br>priority</div>
      <div class="feature"><svg width="44" height="48" viewBox="0 0 44 48" fill="none" stroke="#2f4a23" stroke-width="2"><rect x="8" y="6" width="28" height="38" rx="2"/><rect x="16" y="3" width="12" height="6" fill="#79b540"/><path d="M14 18h4M22 18h10M14 26h4M22 26h10M14 34h4M22 34h10"/></svg>Free<br>estimates</div>
      <div class="feature"><svg width="44" height="48" viewBox="0 0 44 48" fill="none" stroke="#2f4a23" stroke-width="2"><path d="M22 2l3 6 6 1-4 4 1 6-6-3-6 3 1-6-4-4 6-1z" fill="#79b540" stroke="none"/><circle cx="12" cy="28" r="4"/><circle cx="22" cy="26" r="4"/><circle cx="32" cy="28" r="4"/><path d="M4 44c0-6 4-9 8-9s8 3 8 9M14 42c0-6 4-9 8-9s8 3 8 9M24 44c0-6 4-9 8-9s8 3 8 9"/></svg>Licensed arborist<br>on staff</div>
    </div>
  </section>

  <section class="callband">
    <div class="ph" role="img" aria-label="Chainsaw cutting through a mossy tree trunk" style="background:linear-gradient(120deg,#5b5a3a,#8a7446 55%,#c9a77a)"></div>
    <div class="copy">
      <h2><b>Call Us Today</b> To See How We Can Help You<br>With All of Your Tree Needs:</h2>
      <div class="numbers"><svg width="26" height="26" viewBox="0 0 24 24"><path d="M6 2l4 4-2 3c1 3 4 6 7 7l3-2 4 4-3 4C10 21 3 14 2 5z" fill="none" stroke="#79b540" stroke-width="2"/></svg>(555) 014-2739 &nbsp;|&nbsp; (555) 019-9939</div>
      <span class="btn btn-green">Call MARLOWE for a Free Estimate</span>
    </div>
  </section>

  <section class="about">
    <div class="copy">
      <h2>Who We Are</h2>
      <p class="lead">At Quillby Tree Care, we are more than just a tree service company, we are stewards of our beautiful trees.</p>
      <p class="body">With a passion deeply rooted in arboriculture, we embark on a mission to promote the health, beauty, and safety of your trees and landscapes. Whether it's expert tree trimming to enhance aesthetics, meticulous tree removal to mitigate hazards, or comprehensive tree health assessments to ensure safety, we approach each task with unwavering dedication and attention to detail.</p>
      <span class="btn btn-forest">Discover More</span>
    </div>
    <div class="estimate">
      <h3>Get a Free Estimate</h3>
      <div class="fields">
        <div class="field">First name</div><div class="field">Last name</div>
        <div class="field wide">Email...</div>
        <div class="field">ZIP code</div><div class="field">Phone</div>
      </div>
      <p class="terms">You also agree to our <u>Terms of Service.</u></p>
      <span class="btn btn-green">Get a Quote</span>
    </div>
  </section>

  <footer class="footer">
    <div class="wordmark">Quillby Tree Care</div>
    <div class="fcol" style="left:418px">
      <h4>Contact Us</h4>
      <div class="row">☏ (555) 014-2739</div>
      <div class="row">☏ (555) 019-9939</div>
      <div class="row" style="font-size:9.5px">✉ hello@quillbytree.example</div>
      <div class="row" style="font-size:9.5px;line-height:1.9">⌖ 48 Birchwood Lane, Suite 2,<br>Fernvale 30412</div>
    </div>
    <div class="fcol small" style="left:646px">
      <h4>Quick Links</h4>
      Home<br>About Us<br>Services<br>Blog<br>Contact Us
    </div>
    <div class="fcol small" style="left:754px;top:110px">
      Terms and Conditions<br>Privacy Policy
    </div>
    <div class="socials"><span></span><span class="on"></span><span></span><span></span></div>
    <div class="rule"></div>
    <p class="copy">© 2024 <b>Quillby Tree Care.</b> All Rights Reserved</p>
  </footer>

</main>
</body>
</html>
```